13 Tavo - new website design project

Our company Tavo Electrical is developing a new lead generation website focused on Electrical, LED Lighting and Solar Power. We need a high converting website.

Example of our current website is www.tavoelectrical.com.au You can take content from this website for this new design. Our colours are red, black and white. For our new website we would like to promote Tavo, Bright Days Ahead. Please listen to the jingle.

The below link is the company jingle that we have developed.
http://www.tunecraftaudio.com.au/tav-tc-v1/

The key for this brief is to generate leads for Electrical, LED Lighting (for commercial) and Solar Power & Storage.

Target Market(s)

Business owners in Melbourne Victoria

Number of Pages Required

4 page

Colors
ec1f27
ffffff

Requirements
Must have
• This page must be clean, be in line with company branding and a high converting lead website.

```html
<!DOCTYPE html>
<html lang="en">
<head>
<meta charset="utf-8">
<title>Tavo Electrical</title>
<link rel="stylesheet" href="https://fonts.googleapis.com/css2?family=Roboto:wght@300;400;500;700&display=swap">
<style>
:root{
  --red:#ec1f27;
  --red-deep:#c9202a;
  --ink:#333333;
  --muted:#777777;
  --hero-bg:#efeeec;
  --dark:#2e2e2e;
  --dark-line:#4a4a4a;
  --footer:#262626;
  --white:#ffffff;
}
*{box-sizing:border-box;margin:0;padding:0}
html,body{width:1200px;height:3136px;overflow:hidden}
body{font-family:"Roboto",Arial,sans-serif;color:var(--ink);background:var(--white);position:relative}
.abs{position:absolute}

/* header + hero */
.hero{position:absolute;left:0;top:0;width:1200px;height:664px;background:var(--hero-bg)}
.brand{position:absolute;left:136px;top:26px;display:flex;align-items:center;gap:10px}
.brand-mark{width:18px;height:18px;background:var(--red)}
.brand-name{font-weight:700;font-size:34px;letter-spacing:1px;color:var(--ink);line-height:1}
.brand-sub{position:absolute;left:28px;top:40px;font-size:9px;letter-spacing:6px;color:var(--ink)}
.nav{position:absolute;left:510px;top:44px;display:flex;gap:44px;font-size:11px;color:#666;letter-spacing:.5px}
.phone{position:absolute;left:904px;top:38px;display:flex;align-items:center;gap:12px;font-size:20px;font-weight:500;color:var(--red)}
.phone b{color:var(--ink);font-weight:500}
.hero-title{position:absolute;top:176px;width:1200px;text-align:center;color:var(--red);font-size:35px;font-weight:500;letter-spacing:2px}
.hero-sub{position:absolute;top:226px;width:1200px;text-align:center;font-size:16px;color:var(--ink)}
.hero-visual{position:absolute;left:250px;top:252px;width:700px;height:318px;background:radial-gradient(ellipse at center,#ffffff 0%,#e2e3e4 55%,rgba(239,238,236,0) 75%)}

/* service card */
.service{position:absolute;left:136px;top:610px;width:928px;height:385px;background:var(--white);box-shadow:0 2px 14px rgba(0,0,0,.18)}
.service-label{position:absolute;left:52px;top:48px;color:var(--red);font-size:28px;letter-spacing:1px}
.service-rule{position:absolute;left:236px;top:64px;width:560px;height:1px;background:#e2e2e2}
.service-count{position:absolute;right:48px;top:52px;font-size:15px;color:#999;letter-spacing:2px}
.service-photo{position:absolute;left:52px;top:125px;width:296px;height:205px;background:linear-gradient(135deg,#9aa3ab,#d9c9a3 55%,#6d7680)}
.service-title{position:absolute;left:396px;top:118px;font-size:27px;font-weight:400;color:var(--ink)}
.service-lead{position:absolute;left:396px;top:155px;font-size:20px;font-weight:300;color:#666}
.service-text{position:absolute;left:396px;top:205px;width:470px;font-size:11px;line-height:20px;color:#888}
.btn{position:absolute;left:396px;top:292px;width:140px;height:40px;background:var(--red);color:var(--white);font-size:12px;font-weight:700;letter-spacing:1px;display:flex;align-items:center;justify-content:center}

/* about */
.about-title{position:absolute;top:1068px;width:1200px;text-align:center;font-size:32px;font-weight:300;color:#555}
.about-promise{position:absolute;top:1122px;width:1200px;text-align:center;font-size:13px;font-weight:700;color:var(--red);letter-spacing:.6px}
.about-text{position:absolute;left:270px;top:1178px;width:660px;text-align:center;font-size:11px;line-height:23px;color:#888}
.value{position:absolute;top:1294px;width:272px;height:209px;background:var(--white);box-shadow:0 2px 10px rgba(0,0,0,.18);text-align:center}
.value svg{margin-top:28px}
.value p{margin:18px 22px 0;font-size:11px;line-height:20px;color:#888}
.value p b{color:var(--red);font-weight:400}

/* why */
.why{position:absolute;left:0;top:1586px;width:1200px;height:756px;background:var(--dark)}
.why-title{position:absolute;top:60px;width:1200px;text-align:center;font-size:32px;font-weight:300;color:#cfcfcf}
.why-row{position:absolute;left:136px;width:928px;border-top:1px solid var(--dark-line)}
.why-num{position:absolute;font-size:70px;font-weight:300;color:#454545;line-height:1}
.why-head{position:absolute;font-size:28px;font-weight:300;color:#d8d8d8;line-height:30px}
.why-text{position:absolute;font-size:11px;line-height:21px;color:#8a8a8a}

/* testimonial */
.quote{position:absolute;left:136px;top:2258px;width:928px;height:194px;display:flex;box-shadow:0 2px 10px rgba(0,0,0,.15)}
.quote-client{width:292px;background:var(--white);display:flex;flex-direction:column;align-items:center;justify-content:center}
.client-name{display:flex;align-items:center;gap:8px;font-size:20px;font-weight:700;color:#333}
.client-name i{width:14px;height:14px;background:var(--red);display:block}
.client-sub{font-size:9px;letter-spacing:2px;color:#888;margin-top:4px}
.quote-body{flex:1;background:var(--red-deep);color:var(--white);padding:30px 34px}
.quote-body p{font-size:13px;line-height:23px}
.quote-by{margin-top:16px;font-size:13px;font-weight:700}
.quote-role{font-size:11px;margin-top:4px}

/* clients */
.clients-title{position:absolute;top:2484px;width:1200px;text-align:center;font-size:32px;font-weight:300;color:#c2c2c2}
.client{position:absolute;top:2559px;width:213px;height:129px;display:flex;align-items:center;justify-content:center;font-size:22px;font-weight:500}

/* footer */
.footer{position:absolute;left:0;top:2755px;width:1200px;height:381px;background:var(--footer);color:#999}
.footer-brand{position:absolute;left:136px;top:36px;display:flex;align-items:center;gap:8px;font-size:26px;font-weight:700;color:#bbb}
.footer-brand i{width:14px;height:14px;background:#bbb;display:block}
.social{position:absolute;top:40px;width:28px;height:28px;border:1px solid #888}
.footer-rule{position:absolute;left:136px;top:100px;width:928px;height:1px;background:#3b3b3b}
.col{position:absolute;top:140px}
.col h4{font-size:12px;font-weight:700;letter-spacing:1.5px;color:#bbb;margin-bottom:18px}
.col li{list-style:none;font-size:11px;line-height:22px;color:#8a8a8a}
.email{width:240px;height:40px;border:1px solid #555;display:flex;align-items:center;justify-content:space-between;padding:0 14px;font-size:10px;color:#777}
.footer-base{position:absolute;left:136px;top:317px;width:928px;height:1px;background:#3b3b3b}
.copy{position:absolute;left:136px;top:343px;font-size:10px;color:#777}
.base-links{position:absolute;right:136px;top:343px;display:flex;gap:44px;font-size:10px;color:#888}
</style>
</head>
<body>

<section class="hero">
  <div class="brand"><span class="brand-mark"></span><span class="brand-name">TAVO</span><span class="brand-sub">ELECTRICAL</span></div>
  <nav class="nav"><span>HOME</span><span>TAVO STORY</span><span>OUR WORK</span><span>CONTACT US</span></nav>
  <div class="phone">
    <svg width="18" height="18" viewBox="0 0 24 24" fill="none" stroke="#555" stroke-width="2"><path d="M5 3h4l2 5-3 2a12 12 0 0 0 6 6l2-3 5 2v4a2 2 0 0 1-2 2A18 18 0 0 1 3 5a2 2 0 0 1 2-2z"/></svg>
    <span>13 7720 <b>TAVO</b></span>
  </div>
  <h1 class="hero-title">ELECTRICAL. LED LIGHT. SOLAR POWER</h1>
  <p class="hero-sub">Australia's largest fully integrated Electrical &amp; Energy Solution provider.</p>
  <div class="hero-visual" role="img" aria-label="Group of white LED light bulbs and downlights"></div>
</section>

<section class="service">
  <h2 class="service-label">ELECTRICAL</h2>
  <span class="service-rule"></span>
  <span class="service-count">01 / 03</span>
  <div class="service-photo" role="img" aria-label="Electrician working on a switchboard"></div>
  <h3 class="service-title">5 Year Workmanship Warranty</h3>
  <p class="service-lead">Plus a minimum 1 year warranty on all products!</p>
  <p class="service-text">Great value for money, great service and reliability. These are the key foundations that we offer to our customers. All work is covered by a 5 year workmanship warranty and a minimum 1 year warranty on all products.</p>
  <span class="btn">BOOK ONLINE</span>
</section>

<h2 class="about-title">About Us</h2>
<p class="about-promise">OUR PROMISE – QUALITY, RELIABILITY AND CUSTOMERS FIRST</p>
<p class="about-text">Tavo Electrical was formed to be an expert Electricity Contracting Company providing services to all Residential and Commercial Customers. With over 10 years of experience, Tavo Electrical has developed a highly-experienced team of professionals that ensure all our customer expectations are met.</p>

<div class="value" style="left:136px">
  <svg width="40" height="44" viewBox="0 0 40 44" fill="none" stroke="#777" stroke-width="1.4"><circle cx="20" cy="17" r="13"/><circle cx="20" cy="17" r="8"/><path d="M13 28l-4 14 6-3 4 4 1-12M27 28l4 14-6-3-4 4"/></svg>
  <p><b>Quality</b> Our focus is on quality while maintaining great value for money. We are committed to leading the market with the products that we offer our valuable customers</p>
</div>
<div class="value" style="left:463px">
  <svg width="56" height="44" viewBox="0 0 56 44" fill="none" stroke="#777" stroke-width="1.4"><path d="M2 14l10-6 10 4 8-4 10 2 14 6M8 12l14 18 4-2M20 24l6 6 4-2M26 20l8 8 4-2M34 18l8 8 4-4"/></svg>
  <p><b>Reliability</b> You can count on us to get the job done. We are well organised, professional and turn up when we say we will.</p>
</div>
<div class="value" style="left:789px">
  <svg width="44" height="44" viewBox="0 0 44 44" fill="none" stroke="#777" stroke-width="1.4"><circle cx="18" cy="14" r="9"/><path d="M2 40c2-10 8-14 16-14s14 4 16 14z"/><path d="M28 6a9 9 0 0 1 0 16M34 28c4 2 7 6 8 12"/></svg>
  <p><b>Customer First</b> Customers are the key focus of our business. Our highly-experienced team of Consultants and Electricians are dedicated to ensure all customer needs are met.</p>
</div>

<section class="why">
  <h2 class="why-title">Why Choose Us?</h2>

  <div class="why-row" style="top:123px;height:98px">
    <span class="why-num" style="left:0;top:10px">01</span>
    <h3 class="why-head" style="left:0;top:32px">Professional Service</h3>
    <p class="why-text" style="left:370px;top:28px;width:558px">When you hire a Tavo Electrical Electrician you will get a professional and well-presented Electrician that comes skilled and ready to do the job.</p>
  </div>
  <div class="why-row" style="top:221px;height:109px">
    <p class="why-text" style="left:0;top:30px;width:520px">You can buy with confidence as all of our work has a 5 year workmanship guarantee. For your peace of mind, we unconditionally back our electrical work. We will come back to fix any problems at our own expense.</p>
    <span class="why-num" style="left:636px;top:14px">02</span>
    <h3 class="why-head" style="left:636px;top:30px">5 year workmanship<br>guarantee</h3>
  </div>
  <div class="why-row" style="top:330px;height:102px">
    <span class="why-num" style="left:0;top:12px">03</span>
    <h3 class="why-head" style="left:0;top:32px">Value for Money</h3>
    <p class="why-text" style="left:370px;top:26px;width:558px">We provide extremely competitive pricing, which means you get value for money on quality that is comparable to the best in the industry.</p>
  </div>
  <div class="why-row" style="top:432px;height:111px">
    <p class="why-text" style="left:0;top:28px;width:560px">We a committed to reducing carbon emissions by installing Solar Power and upgrading sites to LED Lighting. In addition to reducing the carbon emissions we recycle Fluorescent Tubes, Highbay Globes, Metal and Cardboard.</p>
    <span class="why-num" style="left:636px;top:12px">04</span>
    <h3 class="why-head" style="left:636px;top:30px">Environmentally<br>Friendly</h3>
  </div>
  <div class="why-row" style="top:543px;height:100px">
    <span class="why-num" style="left:0;top:12px">05</span>
    <h3 class="why-head" style="left:0;top:32px">Fully Insured</h3>
    <p class="why-text" style="left:370px;top:34px;width:558px">Tavo Electrical is fully insured and equipped to handle break downs and service call outs.</p>
  </div>
</section>

<section class="quote">
  <div class="quote-client">
    <div class="client-name"><i></i>BOARDLINE SOLUTIONS</div>
    <div class="client-sub">NORWOOD HALE</div>
  </div>
  <div class="quote-body">
    <p>Tavo Electrical was pleasantly efficient, cost effective and delivered the desired results we were after. we look forward to seeing an ongoing benefit from dealing with them when we pay the Electrical bill going forward."</p>
    <div class="quote-by">Dean Carver</div>
    <div class="quote-role">General Manager Boardline</div>
  </div>
</section>

<h2 class="clients-title">Our satisfied clients include...</h2>
<div class="client" style="left:136px;background:#f2f2f2;color:#2f5aa8">Velvetine</div>
<div class="client" style="left:374px;background:#fff200;color:#111">Outback Surplus</div>
<div class="client" style="left:612px;background:#ee3a2c;color:#fff;font-size:18px">Heron Plumbing Supplies</div>
<div class="client" style="left:849px;background:#d6131b;color:#fff">Golden Grill</div>

<footer class="footer">
  <div class="footer-brand"><i></i>TAVO</div>
  <span class="social" style="left:950px;border-color:var(--red)"></span>
  <span class="social" style="left:990px"></span>
  <span class="social" style="left:1032px"></span>
  <span class="footer-rule"></span>
  <div class="col" style="left:136px"><h4>SITE LINKS</h4><ul><li>Led Lighting</li><li>Solar Power</li><li>Electrical</li><li>Career</li></ul></div>
  <div class="col" style="left:360px"><h4>TOP OFFICE LOCATION</h4><ul><li>Terms and Conditions</li><li>Privacy</li></ul></div>
  <div class="col" style="left:618px"><h4>MAKE A CALL</h4><ul><li style="display:flex;align-items:center;gap:8px"><svg width="12" height="12" viewBox="0 0 24 24" fill="none" stroke="#8a8a8a" stroke-width="2"><path d="M5 3h4l2 5-3 2a12 12 0 0 0 6 6l2-3 5 2v4a2 2 0 0 1-2 2A18 18 0 0 1 3 5a2 2 0 0 1 2-2z"/></svg>+137720TAVO</li></ul></div>
  <div class="col" style="left:824px"><h4>EMAIL</h4>
    <div class="email"><span>Email Address*</span><svg width="16" height="16" viewBox="0 0 24 24" fill="none" stroke="#aaa" stroke-width="1.6"><path d="M3 11l18-8-7 18-3-7z"/></svg></div>
  </div>
  <span class="footer-base"></span>
  <p class="copy">© 2017 TAVO Electrical. All Right Reserved.</p>
  <nav class="base-links"><span>Home</span><span>Our Work</span><span>Tavo Story</span><span>Contact</span></nav>
</footer>

</body>
</html>
```